Freelance Translator in Need of a Business Card

I am a freelance Japanese to English translator. I work in the video game localization industry and do literary translation in my spare time. I would like to have both the English word 'Translator' and the Japanese '翻訳者' in the job title. The final design should evoke trust, openness, and reliability.

Target Market(s)

Video game localization companies
Japanese comic book artists

Industry/Entity Type

Business

Contact Information for Business Card

Daniel Ostrowik, Translator
dan.ostrowik@quellbox.net
verolingworks.com
twitter: @verol_tx

Colors

Designer to choose colors to be used in the design.

```html
<!DOCTYPE html>
<html lang="en">
<head>
<meta charset="utf-8">
<title>Daniel Ostrowik — Translator Business Card</title>
<link rel="stylesheet" href="https://fonts.googleapis.com/css2?family=Lato:wght@400;700&family=Noto+Sans+JP:wght@400&display=swap">
<style>
  :root {
    --backdrop: #2c2c2e;
    --card: #1c1c1d;
    --ink: #ffffff;
    --ink-soft: #e6e6e6;
  }
  * { margin: 0; padding: 0; box-sizing: border-box; }
  html, body { width: 1200px; height: 1200px; overflow: hidden; }
  body {
    background: var(--backdrop);
    font-family: "Lato", "Noto Sans JP", sans-serif;
    color: var(--ink);
    position: relative;
  }
  .card {
    position: absolute;
    left: 160px;
    width: 880px;
    height: 460px;
    background: var(--card);
    box-shadow: 0 18px 40px rgba(0,0,0,0.45);
  }
  .card--front { top: 110px; }
  .card--back  { top: 630px; }

  .brand {
    position: absolute;
    display: flex;
    align-items: center;
    gap: 22px;
  }
  .brand__square { background: var(--ink); flex: none; }
  .brand__name {
    font-weight: 700;
    color: var(--ink);
    letter-spacing: 0.04em;
    text-transform: uppercase;
    line-height: 1.15;
  }
  .card--front .brand { right: 60px; bottom: 56px; flex-direction: row-reverse; }
  .card--front .brand__square { width: 110px; height: 110px; }
  .card--front .brand__name { font-size: 20px; text-align: right; }

  .card--back .brand { left: 60px; top: 150px; }
  .card--back .brand__square { width: 140px; height: 140px; }
  .card--back .brand__name { font-size: 22px; }

  .divider {
    position: absolute;
    left: 420px;
    top: 120px;
    width: 3px;
    height: 210px;
    background: var(--ink);
  }
  .details { position: absolute; left: 470px; top: 128px; }
  .details__name { font-size: 30px; font-weight: 700; letter-spacing: 0.01em; }
  .details__title { font-size: 21px; color: var(--ink-soft); margin-top: 2px; }
  .details__title-jp { font-family: "Noto Sans JP", sans-serif; margin-left: 26px; }
  .contact { list-style: none; margin-top: 34px; }
  .contact__item {
    display: flex;
    align-items: center;
    gap: 16px;
    font-size: 23px;
    line-height: 32px;
  }
  .contact__icon { width: 20px; height: 20px; flex: none; }
</style>
</head>
<body>
  <section class="card card--front" aria-label="Card front">
    <div class="brand">
      <div class="brand__square"></div>
      <div class="brand__name">Daniel<br>Ostrowik</div>
    </div>
  </section>

  <section class="card card--back" aria-label="Card back">
    <div class="brand">
      <div class="brand__square"></div>
      <div class="brand__name">Daniel<br>Ostrowik</div>
    </div>
    <div class="divider"></div>
    <div class="details">
      <h1 class="details__name">Daniel Ostrowik</h1>
      <p class="details__title">Translator<span class="details__title-jp" lang="ja">翻訳者</span></p>
      <ul class="contact">
        <li class="contact__item">
          <svg class="contact__icon" viewBox="0 0 20 20" aria-hidden="true">
            <rect x="2" y="5" width="16" height="11" fill="none" stroke="#fff" stroke-width="1.8"/>
            <path d="M2 5 L10 11 L18 5" fill="none" stroke="#fff" stroke-width="1.8"/>
          </svg>
          dan.ostrowik@quellbox.net
        </li>
        <li class="contact__item">
          <svg class="contact__icon" viewBox="0 0 20 20" aria-hidden="true">
            <circle cx="10" cy="10" r="8" fill="none" stroke="#fff" stroke-width="1.6"/>
            <ellipse cx="10" cy="10" rx="3.5" ry="8" fill="none" stroke="#fff" stroke-width="1.4"/>
            <path d="M2 10 H18 M3.5 6 H16.5 M3.5 14 H16.5" stroke="#fff" stroke-width="1.3"/>
          </svg>
          verolingworks.com
        </li>
        <li class="contact__item">
          <svg class="contact__icon" viewBox="0 0 20 20" aria-hidden="true">
            <circle cx="10" cy="10" r="7" fill="#fff"/>
          </svg>
          @verol_tx
        </li>
      </ul>
    </div>
  </section>
</body>
</html>
```